Fundraising Study Day East of England. Lift the January blues!

A flyer to advertise a fundraising event of lectures for dental hygienists and therapists in support of the exemption campaign. Currently dental hygienists and therapists require a prescription to deliver certain treatment or recommend certain toothpastes. If we are successful in the campaign we will be able to treat patients without these restrictions.

Industry/Entity Type

Dental

```html
<!DOCTYPE html>
<html lang="en">
<head>
<meta charset="utf-8">
<title>Fundraising Study Day East of England – Lift the January Blues!</title>
<link rel="stylesheet" href="https://fonts.googleapis.com/css2?family=Oswald:wght@300;500&family=Open+Sans:wght@400;700&display=swap">
<style>
  :root {
    --blue: #1ca6ea;
    --white: #ffffff;
    --ink: #222222;
    --photo-light: #f3f5f6;
    --photo-mid: #dfe3e6;
    --photo-dark: #5a5a5c;
  }
  * { margin: 0; padding: 0; box-sizing: border-box; }
  html, body { width: 848px; height: 1200px; overflow: hidden; background: var(--white); }
  .flyer { position: relative; width: 848px; height: 1200px; font-family: "Open Sans", Arial, sans-serif; color: var(--ink); }

  .header { position: absolute; top: 0; left: 0; width: 848px; height: 207px; background: var(--blue); color: var(--white); text-align: center; font-family: "Oswald", "Arial Narrow", sans-serif; text-transform: uppercase; }
  .header__kicker { position: absolute; top: 52px; width: 100%; font-weight: 300; font-size: 44px; line-height: 1; letter-spacing: 0.5px; }
  .header__title { position: absolute; top: 108px; width: 100%; font-weight: 500; font-size: 72px; line-height: 1; letter-spacing: 1px; }

  .hero { position: absolute; top: 207px; left: 0; width: 848px; height: 390px;
    background: linear-gradient(160deg, var(--photo-light) 0%, var(--photo-mid) 55%, var(--photo-dark) 100%); }

  .details { position: absolute; top: 597px; left: 0; width: 848px; height: 78px; background: var(--blue); color: var(--white); }
  .details__block { position: absolute; top: 11px; font-size: 14.5px; line-height: 19px; }
  .details__label { font-weight: 700; font-size: 17px; line-height: 22px; text-transform: uppercase; }
  .details__date { left: 73px; }
  .details__place { left: 344px; }
  .details__cost { position: absolute; left: 608px; top: 15px; width: 168px; height: 48px; border: 2px solid var(--white); font-weight: 700; font-size: 17.5px; line-height: 44px; text-align: center; }

  .section-title { color: var(--blue); font-weight: 700; font-size: 17px; text-transform: uppercase; line-height: 22px; }
  .description { position: absolute; top: 696px; left: 73px; width: 718px; }
  .description p { font-size: 14.4px; line-height: 20.5px; text-align: justify; }

  .agenda { position: absolute; top: 828px; left: 68px; width: 345px; font-size: 12.6px; line-height: 17px; }
  .agenda--right { top: 838px; left: 441px; width: 335px; }
  .agenda .section-title { margin-bottom: 0; }
  .session { margin-bottom: 16px; text-align: justify; }
  .session__time { font-weight: 700; }

  .footer { position: absolute; top: 1140px; left: 0; width: 848px; height: 60px; background: var(--blue); color: var(--white); font-family: "Oswald", "Arial Narrow", sans-serif; font-weight: 300; font-size: 16.5px; line-height: 40px; text-align: center; }
</style>
</head>
<body>
<main class="flyer">
  <header class="header">
    <h2 class="header__kicker">Fundraising Study Day East of England.</h2>
    <h1 class="header__title">Lift the January Blues!</h1>
  </header>

  <div class="hero" role="img" aria-label="Photograph of a modern dental surgery with a dark leather patient chair and white equipment"></div>

  <section class="details">
    <div class="details__block details__date">
      <div class="details__label">Date and Time</div>
      Fri 19 January 2018<br>09:00 – 16:30 GMT
    </div>
    <div class="details__block details__place">
      <div class="details__label">Location</div>
      Ashford Grange Hotel Meadow Way<br>Hatfield AL10 4QT
    </div>
    <div class="details__cost">Cost - £101.48</div>
  </section>

  <section class="description">
    <h3 class="section-title">Description</h3>
    <p>A fundraising event to support our exemptions project. The day will consist of a series of presentations ranging from the new ECPD to new technologies. The aim, being to enhance our learning and raise funds to support the exemptions campaign. The speaker line includes some of the UK and Irelands most respected dental professionals in our field.</p>
  </section>

  <section class="agenda">
    <h3 class="section-title">Agenda</h3>
    <div class="session"><span class="session__time">9.30 - 10.15</span><br>Helen Marsh: Immediate past president of the AHTA will be updating us on all things ECPD</div>
    <div class="session"><span class="session__time">10.15-11.00</span><br>Leanne Corbett: Will provide an update on teeth whiteing and explain how social media has impacted her business</div>
    <div class="session">Annette Hale: Our internationally acclaimed speaker will update our knowledge of periodontal disease and nutrition and new technologies.</div>
    <div class="session"><span class="session__time">11.00-11.30</span><br>Break</div>
  </section>

  <section class="agenda agenda--right">
    <div class="session"><span class="session__time">11.30-13.00</span> Niamh Doyle &amp; Karen Whitby: Will be providing a combined presentation on 'Scaling your business' and start to finish Sonaclean techniques. The aim being to build our business with effective communications, systems and protocols. This sessions promises audience participation!</div>
    <div class="session"><span class="session__time">12.00-14.00</span> lunch</div>
    <div class="session"><span class="session__time">14.00-15.00</span> &nbsp;Priya Shah: Save your back. All things posture.</div>
    <div class="session"><span class="session__time">15.00-15.30</span> Break</div>
    <div class="session"><span class="session__time">15.30-16.30</span> Annette Hale: Our internationally acclaimed speaker will update our knowledge of periodontal disease and nutrition and new technologies.</div>
  </section>

  <footer class="footer">https://www.ticketlane.co.uk/e/fundraising-study-day-east-of-england-lift-the-january-blues-tickets-48213905716</footer>
</main>
</body>
</html>
```